Business Card Re-Design/Update

We'd like to update out business cards. I've included our current "Style guide" which has the colour scheme of the organisation in it. I've also included the branding files with logos etc in them.

I've also included a copy of one of our existing cards so that you can see how ugly/dated they look. I'd like a fresh modern corporate look.

Target Market(s)

These are for our clients, potential clients, industry contacts - like all business cards

Contact Information for Business Card

Name
Position
Company Address - Level 1, 52 Copperfield Road, Dunmore Qld 4071
Direct Phone
mobile
Email
Website -www.korvelit.com.au
Logo

Colors

Designer to choose colors to be used in the design.

Requirements
Must have
• Main Logo
• Cards will need to be editable to be able to personalize them for each new employee.
Nice to have
• The MapIT, HandIT, KeepIT would be okay to have if they can be sensibly and professionally added to the look without detracting from the main imagery.
• Maybe they could go on the back of the card? will leave this to your creative discretion as to whether/where they fit.
Should not have
• Should not have decorative or script fonts

```html
<!DOCTYPE html>
<html lang="en">
<head>
<meta charset="utf-8">
<title>Korvel Group business card</title>
<link rel="stylesheet" href="https://fonts.googleapis.com/css2?family=Poppins:wght@400;500&display=swap">
<style>
  :root {
    --blue: #1f86d0;
    --black: #050505;
    --white: #ffffff;
    --stage: #d4d4d4;
    --pattern-dark: #0a1420;
    --pattern-light: #11243a;
    --text-light: #f2f2f2;
  }
  * { margin: 0; padding: 0; box-sizing: border-box; }
  html, body { width: 1200px; height: 800px; overflow: hidden; }
  body {
    background: var(--stage);
    font-family: "Poppins", sans-serif;
    display: flex;
    align-items: center;
    justify-content: center;
    gap: 60px;
  }
  .card {
    width: 520px;
    height: 318px;
    position: relative;
    overflow: hidden;
    box-shadow: 0 6px 18px rgba(0,0,0,0.18);
  }
  /* Front */
  .card-front { display: flex; background: var(--black); }
  .front-brand {
    width: 46%;
    background: var(--white);
    display: flex;
    align-items: center;
    justify-content: center;
    position: relative;
  }
  .front-brand::after {
    content: "";
    position: absolute;
    right: -12px;
    top: 64px;
    border-left: 12px solid var(--white);
    border-top: 10px solid transparent;
    border-bottom: 10px solid transparent;
  }
  .wordmark {
    display: flex;
    align-items: center;
    gap: 8px;
    color: var(--blue);
    font-weight: 500;
    letter-spacing: -0.3px;
    white-space: nowrap;
  }
  .wordmark-mark { background: var(--blue); flex: none; }
  .front-brand .wordmark { font-size: 27px; }
  .front-brand .wordmark-mark { width: 20px; height: 20px; }
  .front-details {
    flex: 1;
    padding: 52px 24px 0 36px;
    color: var(--text-light);
  }
  .person-name {
    color: var(--blue);
    font-size: 19px;
    font-weight: 400;
    letter-spacing: 0.5px;
    text-transform: uppercase;
    line-height: 1.1;
  }
  .person-role { font-size: 11px; margin-top: 2px; }
  .address { font-size: 11px; line-height: 1.45; margin-top: 14px; }
  .contact-list { list-style: none; margin-top: 14px; }
  .contact-list li {
    display: flex;
    align-items: center;
    gap: 8px;
    font-size: 11px;
    line-height: 1.75;
  }
  .contact-list svg { width: 10px; height: 10px; flex: none; }
  .accent { color: var(--blue); }
  /* Back */
  .card-back { background: var(--black); display: flex; align-items: center; justify-content: center; }
  .back-pattern {
    position: absolute;
    inset: 0;
    background: radial-gradient(circle at 50% 50%, var(--pattern-light), var(--pattern-dark) 70%, var(--black));
  }
  .card-back .wordmark { position: relative; font-size: 40px; gap: 12px; }
  .card-back .wordmark-mark { width: 32px; height: 32px; }
</style>
</head>
<body>
  <section class="card card-front" aria-label="Business card front">
    <div class="front-brand">
      <div class="wordmark"><span class="wordmark-mark"></span><span>Korvel Group</span></div>
    </div>
    <div class="front-details">
      <h1 class="person-name">Mara Ellison</h1>
      <p class="person-role">Business Development Manager</p>
      <p class="address">Level 1, 52 Copperfield Road,<br>Dunmore Qld 4071</p>
      <ul class="contact-list">
        <li><svg viewBox="0 0 10 10"><rect x="2.5" y="0.5" width="5" height="9" rx="1" fill="none" stroke="#1f86d0"/></svg><span>+61 (0)412 507 318</span></li>
        <li><svg viewBox="0 0 10 10"><rect x="1" y="4" width="8" height="5" fill="#1f86d0"/><rect x="3" y="1" width="4" height="3" fill="none" stroke="#1f86d0"/></svg><span>+61 (0)7 3180 4426</span></li>
        <li><svg viewBox="0 0 10 10"><path d="M2 1 L4 1 L4.6 3 L3.4 4 Q4.5 6 6 6.6 L7 5.4 L9 6 L9 8 Q5 9 2 5.5 Q1 3 2 1Z" fill="#1f86d0"/></svg><span>+61 (0)7 3180 4400</span></li>
        <li><svg viewBox="0 0 10 10"><rect x="1" y="3.5" width="8" height="5.5" fill="#1f86d0"/><rect x="2.5" y="1" width="5" height="3" fill="#1f86d0"/></svg><span>+61 (0)7 3180 4409</span></li>
        <li><svg viewBox="0 0 10 10"><rect x="0.5" y="2" width="9" height="6" fill="none" stroke="#1f86d0"/><path d="M0.5 2 L5 5.5 L9.5 2" fill="none" stroke="#1f86d0"/></svg><span>mellison@korvelit.com.au</span></li>
        <li><svg viewBox="0 0 10 10"><circle cx="5" cy="5" r="4.5" fill="#1f86d0"/><path d="M0.5 5 H9.5 M5 0.5 V9.5" stroke="#050505" stroke-width="0.8"/></svg><span>www.<span class="accent">korvelit</span>.com.au</span></li>
      </ul>
    </div>
  </section>

  <section class="card card-back" aria-label="Business card back">
    <div class="back-pattern" role="img" aria-label="Faint repeating brand symbol pattern on black"></div>
    <div class="wordmark"><span class="wordmark-mark"></span><span>Tandem Service</span></div>
  </section>
</body>
</html>
```